GLP letterhead

We need a letterhead design for our new company based in Los Angeles called "Gold Lantern Pictures". We develop film and television projects. We work with investors, financiers, film production companies, film distribution and sales companies as well as studios. We would like to incorporate our logo (see attached) but make the letterhead simple and elegant. We need to include: logo, company address, phone number and company website.
Updates

Hello designers, Thanks for your submissions. For our letterhead, we are looking for something more simple and elegant. No heavy bars or lines. Make it feel light and clean. Not a lot of ink on the page. Use the logo and contact info but think "clean", "streamlined" and mostly white paper. Looking forward to seeing more... thanks! Gold Lantern Pictures team

Target Market(s)

Studio executives, talent agents and agencies, financiers, investors.

Industry/Entity Type

It Company

Requirements
Must have
• Gold Lantern Pictures logo (see attached). Logo may be cropped and altered appropriately for elegant letterhead design.
• Please include:
• COMPANY ADDRESS:
• Ridgeway Studio Park
• 2850 Halverson Street
• Tower Annex, 4th Floor
• Manhattan Beach, CA 90412
• COMPANY WEBSITE:
• www.goldlanternpicturesco.example
• COMPANY PHONE NUMBER:
• 310-555-0148

```html
<!DOCTYPE html>
<html lang="en">
<head>
<meta charset="utf-8">
<title>Gold Lantern Pictures — Letterhead</title>
<link rel="stylesheet" href="https://fonts.googleapis.com/css2?family=Open+Sans:wght@400;600&display=swap">
<style>
  :root {
    --backdrop: #e9e9e9;
    --paper: #ffffff;
    --brand-blue: #1aa7e0;
    --brand-dark: #0d2a35;
    --tab-dark: #2b2b2b;
    --text-gray: #4a4a4a;
    --icon-blue: #3b6fb0;
  }
  html, body {
    margin: 0;
    padding: 0;
    width: 950px;
    height: 1200px;
    overflow: hidden;
    background: var(--backdrop);
    font-family: "Open Sans", Arial, sans-serif;
  }
  .letterhead {
    position: absolute;
    left: 50px;
    top: 50px;
    width: 850px;
    height: 1100px;
    background: var(--paper);
    box-shadow: 0 1px 4px rgba(0,0,0,0.12);
  }
  .brand {
    position: absolute;
    left: 0;
    right: 0;
    top: 18px;
    text-align: center;
  }
  .brand-disc {
    display: block;
    width: 130px;
    height: 130px;
    margin: 0 auto;
    border-radius: 50%;
    background: var(--brand-dark);
  }
  .brand-name {
    margin: 14px 0 0;
    font-size: 22px;
    font-weight: 600;
    letter-spacing: 1px;
    color: var(--brand-blue);
  }
  .tab {
    position: absolute;
  }
  .tab-left {
    left: 0;
    top: 990px;
    width: 16px;
    height: 93px;
    background: var(--brand-blue);
    border-radius: 0 10px 10px 0;
  }
  .tab-right {
    right: 0;
    top: 1005px;
    width: 15px;
    height: 63px;
    background: var(--tab-dark);
    border-radius: 10px 0 0 10px;
  }
  .address {
    position: absolute;
    left: 26px;
    top: 1009px;
    margin: 0;
    font-style: normal;
    font-size: 15.5px;
    line-height: 24px;
    color: var(--text-gray);
  }
  .contact {
    position: absolute;
    right: 29px;
    top: 1009px;
    margin: 0;
    padding: 0;
    list-style: none;
    text-align: right;
    font-size: 15.5px;
    line-height: 24px;
    color: var(--text-gray);
  }
  .contact li {
    display: flex;
    justify-content: flex-end;
    align-items: center;
    gap: 6px;
  }
  .contact svg {
    width: 13px;
    height: 13px;
  }
</style>
</head>
<body>
  <main class="letterhead">
    <header class="brand">
      <span class="brand-disc"></span>
      <p class="brand-name">Gold Lantern Pictures</p>
    </header>

    <footer>
      <span class="tab tab-left"></span>
      <address class="address">
        Ridgeway Studio Park 2850 Halverson Street Tower Annex,<br>
        4th Floor Manhattan Beach, CA 90412
      </address>
      <ul class="contact">
        <li>
          <svg viewBox="0 0 16 16" aria-hidden="true">
            <circle cx="8" cy="8" r="7" fill="none" stroke="var(--icon-blue)" stroke-width="1.2"/>
            <path d="M5.5 4.5c-.8.8-.6 2.6 1 4.5s3.7 2.4 4.5 1.6l-1.3-1.3-1 .6c-.6-.3-1.5-1.2-1.8-1.8l.6-1z" fill="var(--icon-blue)"/>
          </svg>
          <span>310-555-0148</span>
        </li>
        <li>
          <svg viewBox="0 0 16 16" aria-hidden="true">
            <g fill="none" stroke="var(--icon-blue)" stroke-width="1">
              <circle cx="8" cy="8" r="7"/>
              <ellipse cx="8" cy="8" rx="3" ry="7"/>
              <line x1="1" y1="8" x2="15" y2="8"/>
              <line x1="2.2" y1="4.5" x2="13.8" y2="4.5"/>
              <line x1="2.2" y1="11.5" x2="13.8" y2="11.5"/>
            </g>
          </svg>
          <span>www.goldlanternpicturesco.example</span>
        </li>
      </ul>
      <span class="tab tab-right"></span>
    </footer>
  </main>
</body>
</html>
```